High End Mechanic Business Card Design Project

Automotive Business - Repair, service and sales
Bold background with clarity of text

Industry/Entity Type

Automotive

Contact Information for Business Card

Black background with silver or white kvt 418 lorne coupe at the bottom right angered with the business name and address at the top left.. Also to include a compass near the business name and the text... Sales Service RepairAdded photos as EXAMPLES. Don't want the actual n, s, e w on the compass picture but to know that it is a compass.

Font styles to use
Sans Serif

Requirements
Must have
• Creativity, black background, Images: 4 Lorne KVT Coupe & Compass (without text)

```html
<!DOCTYPE html>
<html lang="en">
<head>
<meta charset="utf-8">
<title>Harrowgate North Motors – Business Card</title>
<link rel="stylesheet" href="https://fonts.googleapis.com/css2?family=Exo+2:wght@300;400;600;700&display=swap">
<style>
  :root {
    --page: #d9d6d1;
    --card: #0b0b0c;
    --card-edge: #1c1c1e;
    --silver: #e6e7ea;
    --silver-dim: #b9bbc0;
    --accent: #ec7a5c;
    --photo-light: #e9ecef;
    --photo-mid: #9ea4ab;
    --photo-dark: #2b2e33;
  }
  * { box-sizing: border-box; margin: 0; padding: 0; }
  html, body {
    width: 1200px; height: 900px; overflow: hidden;
    background: var(--page);
    font-family: "Exo 2", sans-serif;
  }
  .stage {
    width: 1200px; height: 900px;
    display: flex; align-items: center; justify-content: center;
  }
  .business-card {
    position: relative;
    width: 1000px; height: 572px;
    background: radial-gradient(ellipse at 30% 20%, #1d1d20 0%, var(--card) 60%);
    border: 1px solid var(--card-edge);
    border-radius: 6px;
    box-shadow: 0 18px 40px rgba(0,0,0,.35);
    color: var(--silver);
    overflow: hidden;
  }
  .brand-mark {
    position: absolute; left: 56px; top: 76px;
    width: 170px; height: 170px;
    border: 14px solid var(--silver-dim);
    border-radius: 50%;
  }
  .brand {
    position: absolute; left: 256px; top: 74px;
    width: 410px;
  }
  .brand-name {
    font-weight: 600;
    color: var(--silver);
    text-transform: uppercase;
    line-height: 1;
  }
  .brand-name .line-small { display: block; font-size: 30px; letter-spacing: 3px; }
  .brand-name .line-large { display: block; font-size: 88px; letter-spacing: 2px; margin-top: 4px; }
  .brand-rule {
    width: 100%; height: 2px; background: var(--silver-dim);
    margin: 10px 0 10px;
  }
  .services {
    font-size: 26px; font-weight: 400; letter-spacing: 1.5px;
    color: var(--accent); text-transform: uppercase;
    white-space: nowrap;
  }
  .car-photo {
    position: absolute; right: 40px; top: 70px;
    width: 250px; height: 290px;
    border-radius: 4px;
    background: radial-gradient(ellipse at 50% 50%, var(--photo-light) 0%, var(--photo-mid) 45%, var(--photo-dark) 75%, var(--card) 100%);
  }
  .specialty {
    position: absolute; right: 25px; top: 385px;
    width: 280px; text-align: center;
    font-size: 21px; letter-spacing: 1.5px;
    color: var(--accent); text-transform: uppercase;
    white-space: nowrap;
  }
  .contact {
    position: absolute; left: 256px; bottom: 60px;
    font-style: normal;
    font-size: 24px; letter-spacing: 1.5px; text-transform: uppercase;
    line-height: 1.3;
    color: var(--silver);
  }
  .contact .phone {
    display: flex; align-items: center; gap: 14px;
    font-size: 40px; font-weight: 300; margin-top: 8px;
  }
  .phone-icon { width: 30px; height: 30px; flex: none; }
</style>
</head>
<body>
<main class="stage">
  <section class="business-card">
    <div class="brand-mark" aria-hidden="true"></div>

    <header class="brand">
      <h1 class="brand-name">
        <span class="line-small">Harrowgate North</span>
        <span class="line-large">Motors</span>
      </h1>
      <div class="brand-rule"></div>
      <p class="services">Sales | Service | Repair</p>
    </header>

    <div class="car-photo" role="img" aria-label="Photo of a white KVT 4 Lorne coupe, front three-quarter view"></div>
    <p class="specialty">European &amp; Domestic</p>

    <address class="contact">
      <span>1280 Alder Ridge Blvd.</span><br>
      <span>Dalton, GA 30720</span>
      <span class="phone">
        <svg class="phone-icon" viewBox="0 0 30 30" aria-hidden="true">
          <rect x="0" y="0" width="30" height="30" rx="5" fill="var(--silver)"/>
          <path d="M10 7c1 0 2 3 2 4s-1.5 1.5-1.5 2.5c1 2.5 3 4.5 5.5 5.5 1 0 1.5-1.5 2.5-1.5s4 1 4 2-1 4-3 4C12 23 7 18 7 10c0-2 2-3 3-3z" fill="var(--card)"/>
        </svg>
        555.204.7316
      </span>
    </address>
  </section>
</main>
</body>
</html>
```